Kestrel Shore Camp

We need a web page that details location/distance to Melbourne, the facilities available, the magnificent setting, contact information, history of the area and our background in the industry booking enquiry page linked to our email account, feedback page.
(Refer www.campdunmorecove.com.au for details and further imagary as we operate in the same facility and Camp Dunmore Cove Business no longer exists) WE WANT A BETTER WEBSITE THAN THIS!!

```html
<!DOCTYPE html>
<html lang="en">
<head>
<meta charset="utf-8">
<title>Kestrel Shore Camp</title>
<link href="https://fonts.googleapis.com/css2?family=Open+Sans:wght@400;600;700&family=PT+Sans:wght@400;700&display=swap" rel="stylesheet">
<style>
:root{
  --orange:#e8870e;
  --orange-dark:#c9700a;
  --ink:#3a3a3a;
  --muted:#9a9a9a;
  --blue:#1f8ec4;
  --nav-home:#2a2624;
  --footer:#403f3e;
  --footer-text:#a9a9a9;
  --panel:#fbfbfb;
  --line:#ececec;
}
*{box-sizing:border-box;margin:0;padding:0}
html,body{width:947px;height:1200px;overflow:hidden}
body{position:relative;font-family:"Open Sans",sans-serif;color:var(--ink);background:#f3f1ee}
.backdrop{position:absolute;inset:0;background:linear-gradient(180deg,#3fa9e6 0%,#8fd0f3 30%,#cfe6ee 48%,#ece6dc 62%,#f1ece4 100%)}
.abs{position:absolute}
.brand{left:0;width:947px;top:14px;text-align:center}
.brand-mark{display:inline-block;width:46px;height:46px;border-radius:50%;background:var(--orange)}
.brand-name{display:block;margin-top:8px;font-family:"PT Sans",sans-serif;font-weight:700;font-size:21px;color:var(--orange)}
.nav{left:136px;top:123px;width:677px;height:42px;background:var(--orange);display:flex;border-radius:3px 3px 0 0;overflow:hidden}
.nav-home{width:58px;background:var(--nav-home);display:flex;align-items:center;justify-content:center}
.nav ul{list-style:none;display:flex;align-items:center;padding-left:6px}
.nav li{font-size:11.5px;color:#fff;padding:0 15px;line-height:42px;border-right:1px solid rgba(255,255,255,.18)}
.nav li:last-child{border-right:0}
.hero{left:136px;top:165px;width:677px;height:333px;background:linear-gradient(160deg,#5b6a4a 0%,#2f6fa8 22%,#1c5d98 50%,#3f86b2 70%,#d9d2bf 80%,#5c7d3f 90%,#3b5a2a 100%)}
.hero-title{left:199px;top:258px;color:#fff;font-weight:700;line-height:1}
.hero-title .l1{display:block;font-size:45px}
.hero-title .l2{display:block;font-size:31px;margin-top:10px}
.dots{left:202px;top:365px;display:flex;gap:4px}
.dots span{width:10px;height:10px;border-radius:50%;border:2px solid #fff;background:#333}
.dots span.on{background:#2a9fd8}
.main{left:136px;top:498px;width:677px;height:497px;background:var(--panel)}
.h-welcome{left:155px;top:512px;font-family:"PT Sans",sans-serif;font-size:17px;font-weight:400;color:var(--ink)}
.h-welcome em{font-style:normal;color:var(--blue)}
.photo{background:linear-gradient(180deg,#8fb3cf,#c9b89a)}
.body-text{font-size:8.6px;line-height:15.5px;color:var(--muted);text-align:justify}
.h-side{left:599px;top:512px;font-family:"PT Sans",sans-serif;font-size:15px;color:#555}
.history{left:596px;top:548px;width:200px;height:133px;border:1px solid var(--line);background:#fff;padding:8px 8px 0 12px}
.history li{list-style:none;font-size:8.6px;line-height:16px;color:#777;padding-left:12px;position:relative;margin-bottom:4px}
.history li::before{content:"›";position:absolute;left:0;top:0;color:#888}
.h-setting{left:154px;top:704px;font-family:"PT Sans",sans-serif;font-size:16px;color:var(--blue);font-weight:400}
.item-title{font-family:"PT Sans",sans-serif;font-size:12px;color:#666}
.read-more{font-size:8.6px;color:#555}
.facilities{left:597px;top:709px;width:199px;height:257px;background:#fff;border:1px solid var(--line)}
.fac-photo{height:128px;background:linear-gradient(180deg,#c8d9e6 0%,#c9a86a 45%,#7a8f52 100%)}
.fac-title{font-family:"PT Sans",sans-serif;font-size:12px;color:#555;margin:15px 0 0 15px}
.fac-text{margin:10px 15px 0}
.footer{left:136px;top:995px;width:677px;height:151px;background:var(--footer)}
.f-head{font-size:11px;color:var(--footer-text);letter-spacing:.2px}
.f-links li{list-style:none;font-size:8.6px;line-height:15.6px;color:var(--footer-text)}
.contact-row{display:flex;align-items:flex-start;gap:10px;font-size:8.6px;line-height:15px;color:var(--footer-text)}
.contact-icon{width:22px;height:22px;border-radius:50%;background:#4c4b4a;display:flex;align-items:center;justify-content:center;flex:none}
.map{left:544px;top:1009px;width:251px;height:120px;background:linear-gradient(135deg,#f7efe3,#f3e7d5 60%,#bcd8ee)}
.copyright{left:138px;top:1164px;font-size:8.6px;color:#444}
.social{left:450px;top:1160px;display:flex;gap:5px}
.social span{width:20px;height:20px;border-radius:50%}
.bottom-links{left:616px;top:1164px;font-size:8.6px;color:#555;word-spacing:1px}
</style>
</head>
<body>
<div class="backdrop" role="img" aria-label="Sunny beach with umbrellas, loungers and a volleyball net under a blue sky"></div>

<div class="abs brand">
  <span class="brand-mark"></span>
  <span class="brand-name">Kestrel Shore Camp</span>
</div>

<nav class="abs nav">
  <div class="nav-home">
    <svg width="14" height="13" viewBox="0 0 14 13"><path d="M7 0L0 6h2v7h4V9h2v4h4V6h2z" fill="#fff"/></svg>
  </div>
  <ul>
    <li>Accommodation</li><li>Activities</li><li>Menu</li><li>Private Camps</li><li>History</li><li>Where we are</li><li>Contact</li>
  </ul>
</nav>

<section class="abs hero" role="img" aria-label="Aerial view of a curved bay with blue water, a sandy beach and green bushland"></section>
<h1 class="abs hero-title"><span class="l1">Kestrel</span><span class="l2">Shore Camp</span></h1>
<div class="abs dots"><span class="on"></span><span></span><span></span><span></span></div>

<main class="abs main"></main>

<h2 class="abs h-welcome">Welcome To <em>Kestrel Shore Camp</em></h2>
<div class="abs photo" style="left:153px;top:548px;width:138px;height:133px" role="img" aria-label="Long sandy beach with distant hills"></div>
<p class="abs body-text" style="left:301px;top:545px;width:269px">Lorem ipsum dolor sit amet, consectetur adipiscing elit, sed do eiusmod tempor incididunt ut labore et dolore magna aliqua. Ut enim ad minim veniam, quis nostrud exercitation ullamco laboris nisi ut aliquip ex ea commodo consequat. Duis aute irure dolor in reprehenderit in voluptate velit esse cillum dolore eu fugiat nulla pariatur. Excepteur sint occaecat cupidatat non proident, sunt in culpa qui officia deserunt mollit anim id est laborum Lorem ipsum dolor sit amet, consectetur adipiscing elit, sed do eiusmod tempor incididunt ut labore et dolore magna aliqua.</p>

<h2 class="abs h-side">History of the area</h2>
<ul class="abs history">
  <li>Experienced Leaders, Day &amp; Night</li>
  <li>Comprehensive &amp; Challenging Programs</li>
  <li>Ensuite Lodge, Under One Roof for Security &amp; Supervision</li>
  <li>Professional Friendly Service</li>
  <li>Top Quality Food &amp; Lots of it!</li>
</ul>

<h2 class="abs h-setting">The Magnificent Setting</h2>

<div class="abs photo" style="left:153px;top:754px;width:138px;height:97px;background:linear-gradient(160deg,#2e6da3,#3a82b8 50%,#d8d0bb 65%,#5e8a45)" role="img" aria-label="Aerial view of the bay and coastline"></div>
<h3 class="abs item-title" style="left:309px;top:751px">Sed do eiusmod tempor incididunt ut labore</h3>
<p class="abs body-text" style="left:309px;top:774px;width:262px">Lorem ipsum dolor sit amet, consectetur adipiscing elit, sed do eiusmod tempor incididunt ut labore et dolore magna aliqua. Ut enim ad minim veniam, quis nostrud exercitation ullamco laboris nisi ut aliquip ex ea commodo consequat.</p>
<span class="abs read-more" style="left:309px;top:841px">Read More +</span>

<div class="abs photo" style="left:153px;top:870px;width:138px;height:96px;background:linear-gradient(160deg,#c7d6df,#8c7a62 50%,#6f8a4e)" role="img" aria-label="Campers on an outdoor climbing activity"></div>
<h3 class="abs item-title" style="left:309px;top:866px">Sed ut perspiciatis unde omnis iste natus</h3>
<p class="abs body-text" style="left:309px;top:889px;width:262px">Lorem ipsum dolor sit amet, consectetur adipiscing elit, sed do eiusmod tempor incididunt ut labore et dolore magna aliqua. Ut enim ad minim veniam, quis nostrud exercitation ullamco laboris nisi ut aliquip ex ea commodo consequat.</p>
<span class="abs read-more" style="left:309px;top:956px">Read More +</span>

<article class="abs facilities">
  <div class="fac-photo" role="img" aria-label="Single-storey lodge building with a long veranda and lawn"></div>
  <h3 class="fac-title">The Facilities Available</h3>
  <p class="body-text fac-text">Lorem ipsum dolor sit amet, consectetur adipiscing elit, sed do eiusmod tempor incididunt ut labore et dolore magna aliqua. Ut enim ad minim veniam, quis nostrud exercitation ullamco laboris nisi</p>
</article>

<footer class="abs footer"></footer>
<h4 class="abs f-head" style="left:152px;top:1010px;font-weight:400">LINKS</h4>
<ul class="abs f-links" style="left:153px;top:1036px">
  <li>Accommodation</li><li>Activities</li><li>Menu</li><li>Private Camps</li><li>History</li>
</ul>
<h4 class="abs f-head" style="left:310px;top:1010px;font-weight:400">GET IN TOUCH</h4>
<div class="abs contact-row" style="left:305px;top:1036px;width:160px">
  <span class="contact-icon"><svg width="8" height="11" viewBox="0 0 8 11"><path d="M4 0a4 4 0 0 0-4 4c0 3 4 7 4 7s4-4 4-7a4 4 0 0 0-4-4zm0 5.5A1.5 1.5 0 1 1 4 2.5a1.5 1.5 0 0 1 0 3z" fill="#777"/></svg></span>
  <span>14 Tern St. Dunmore Cove, Victoria 3960</span>
</div>
<div class="abs contact-row" style="left:305px;top:1073px">
  <span class="contact-icon"><svg width="10" height="9" viewBox="0 0 10 9"><path d="M1 2h8v6H1z M3 0h4v2H3z" fill="#777"/></svg></span>
  <span style="line-height:22px">Toll free: (03) 5550 0192</span>
</div>
<div class="abs contact-row" style="left:305px;top:1102px">
  <span class="contact-icon"><svg width="10" height="7" viewBox="0 0 10 7"><path d="M0 0h10v7H0z" fill="#777"/><path d="M0 0l5 4 5-4" stroke="#4c4b4a" fill="none"/></svg></span>
  <span style="line-height:22px">campkestrelshore@shoremail.com</span>
</div>
<div class="abs map" role="img" aria-label="Locality map showing the road route from Melbourne through nearby towns to the camp"></div>

<p class="abs copyright">©2014 Kestrel Shore Camp, All Rights Reserved.</p>
<div class="abs social" aria-label="Social links">
  <span style="background:#3b5998"></span><span style="background:#2fa3d9"></span><span style="background:#ef6b2a"></span><span style="background:#c4302b"></span>
</div>
<p class="abs bottom-links">Home &nbsp;&nbsp;| &nbsp;&nbsp;About &nbsp;&nbsp;| &nbsp;Private Camps | &nbsp;Contacts</p>
</body>
</html>
```